Flyer for customer acquisition.

Hello, We are a sportmanagement agency from Germany and we need information flyers for customer acquisition. It should be DinA4 and should have a modern but serious design. I have uploaded a information sheet, where you can find the text and the composition, the flyer should have. I also uploaded Pictures / Images, which you can use. Of course you can use other suitable images. If they are not free, I will buy them later. On the bottom of the flyer there has been the contact information. You will find them in the download section, too. If you have questions, just write me. If I forgot something, I will update the letter :) Thank you very much!
Ich brauche zusätzliche Tage um durchzusehen

```html
<!DOCTYPE html>
<html lang="de">
<head>
<meta charset="utf-8">
<title>SVR-P Nachwuchsförderung und Management</title>
<link href="https://fonts.googleapis.com/css2?family=Open+Sans:wght@400;800&family=PT+Sans:wght@400&display=swap" rel="stylesheet">
<style>
  :root{
    --sky:#4fcdf0;
    --ink:#1e1e1e;
    --white:#ffffff;
    --grass:#a6dc4f;
    --text:#222222;
  }
  *{margin:0;padding:0;box-sizing:border-box}
  html,body{width:934px;height:1200px;overflow:hidden;background:var(--white)}
  body{font-family:"PT Sans",Arial,sans-serif;color:var(--text)}
  .flyer{position:relative;width:934px;height:1200px;overflow:hidden;background:var(--white)}
  .backdrop{position:absolute;left:0;top:0}

  .tagline{position:absolute;left:50px;top:122px;color:var(--white);font-family:"Open Sans",Arial,sans-serif;font-size:19px;line-height:30px;font-weight:400}
  .tagline .boxed{display:inline-block;background:var(--white);color:var(--sky);margin-left:-50px;padding-left:50px;width:170px;line-height:29px}

  .headline{position:absolute;left:58px;top:240px;color:var(--white);font-family:"Open Sans",Arial,sans-serif;font-weight:800;font-size:68px;line-height:77px;letter-spacing:-5px;text-shadow:3px 3px 2px rgba(79,205,240,.75)}

  .services{list-style:none;font-size:11px}
  .services li{position:relative;padding-left:11px}
  .services li::before{content:"*";position:absolute;left:0;top:1px;font-size:13px}
  .services .title{display:block}

  .services-right{position:absolute;left:650px;top:608px;width:224px;line-height:17.4px}
  .services-bottom{position:absolute;top:886px;line-height:16.4px}
  .col-1{left:56px;width:266px}
  .col-2{left:336px;width:262px}
  .col-3{left:616px;width:268px}

  .brand{position:absolute;left:70px;top:990px;width:160px;height:40px;display:flex;align-items:center;justify-content:center;gap:10px}
  .brand-dot{width:16px;height:16px;border-radius:50%;background:var(--ink)}
  .brand-name{font-family:"Open Sans",Arial,sans-serif;font-size:28px;font-weight:800;color:var(--ink);letter-spacing:1px}

  .contact{position:absolute;left:50px;top:1068px;list-style:none;font-family:"Open Sans",Arial,sans-serif;font-size:20px;line-height:26.5px;color:var(--ink)}
  .contact li{display:flex;align-items:center;gap:13px}
  .contact svg{flex:none}

  .rule{position:absolute;left:244px;top:1022px;width:618px;height:5px;background:var(--sky)}
  .footnote{position:absolute;left:264px;top:1036px;width:620px;font-family:"Open Sans",Arial,sans-serif;font-size:9.6px;line-height:21px;color:var(--text)}
  .footnote-extra{position:absolute;right:53px;top:1148px;font-family:"Open Sans",Arial,sans-serif;font-size:9.6px;color:var(--text)}

  .footer-bar{position:absolute;top:1173px;height:27px}
  .bar-1{left:409px;width:164px;background:var(--sky)}
  .bar-2{left:573px;width:105px;background:var(--ink)}
  .bar-3{left:678px;width:92px;background:var(--sky)}
  .bar-4{left:770px;width:92px;background:var(--ink)}
</style>
</head>
<body>
<main class="flyer">
  <svg class="backdrop" width="934" height="1200" viewBox="0 0 934 1200">
    <defs>
      <linearGradient id="team-tone" x1="0" y1="0" x2="0" y2="1">
        <stop offset="0" stop-color="#cfcfcf"/>
        <stop offset=".28" stop-color="#b9b9b9"/>
        <stop offset=".42" stop-color="#4a4a4a"/>
        <stop offset="1" stop-color="#1c1c1c"/>
      </linearGradient>
      <linearGradient id="lawn" x1="0" y1="0" x2="0" y2="1">
        <stop offset="0" stop-color="var(--grass)"/>
        <stop offset=".55" stop-color="#cdeb9c"/>
        <stop offset="1" stop-color="var(--white)"/>
      </linearGradient>
      <linearGradient id="pieces-fade" x1="0" y1="0" x2="1" y2="0">
        <stop offset="0" stop-color="#86c93a" stop-opacity="0"/>
        <stop offset=".08" stop-color="#86c93a" stop-opacity=".8"/>
        <stop offset=".85" stop-color="#86c93a" stop-opacity=".8"/>
        <stop offset="1" stop-color="#86c93a" stop-opacity="0"/>
      </linearGradient>
      <radialGradient id="player-tone" cx=".5" cy=".45" r=".6">
        <stop offset="0" stop-color="#b59ae0"/>
        <stop offset=".5" stop-color="#e4e2ee"/>
        <stop offset="1" stop-color="#f2f2f2"/>
      </radialGradient>
      <linearGradient id="training-tone" x1="0" y1="0" x2="0" y2="1">
        <stop offset="0" stop-color="#bfe3ef"/>
        <stop offset=".55" stop-color="#8fc45a"/>
        <stop offset="1" stop-color="#c9d6e2"/>
      </linearGradient>
      <radialGradient id="kids-tone" cx=".45" cy=".5" r=".6">
        <stop offset="0" stop-color="#e08a3c"/>
        <stop offset=".45" stop-color="#4f9b3f"/>
        <stop offset="1" stop-color="#6da94a"/>
      </radialGradient>
    </defs>

    <rect width="934" height="900" fill="var(--sky)"/>
    <path d="M0 608 C300 600 620 588 934 545 L934 900 L0 900 Z" fill="url(#lawn)"/>
    <rect role="img" aria-label="Illustration: Schachfiguren aus Rasen" x="156" y="672" width="520" height="170" rx="26" fill="url(#pieces-fade)"/>
    <path d="M0 232 C120 205 240 195 320 200 L460 620 C340 560 160 505 0 505 Z" fill="var(--ink)"/>
    <path role="img" aria-label="Foto: drei Berater in Anzügen vor grauem Hintergrund" d="M270 0 L934 0 L934 350 C820 470 640 580 448 612 C360 520 300 300 270 0 Z" fill="url(#team-tone)"/>

    <circle cx="226" cy="624" r="32" fill="var(--white)"/>
    <circle cx="398" cy="580" r="106" fill="var(--white)"/>
    <circle role="img" aria-label="Illustration: farbenfroher Fußballspieler mit Ball" cx="398" cy="580" r="88" fill="url(#player-tone)"/>
    <circle cx="324" cy="738" r="70" fill="var(--sky)"/>
    <circle cx="324" cy="738" r="61" fill="var(--white)"/>
    <circle role="img" aria-label="Foto: Trainingsplatz mit Fußbällen" cx="324" cy="738" r="56" fill="url(#training-tone)"/>
    <circle cx="524" cy="730" r="82" fill="var(--white)"/>
    <circle role="img" aria-label="Foto: Kinder beim Fußballspiel" cx="524" cy="730" r="70" fill="url(#kids-tone)"/>
  </svg>

  <div class="tagline">SVR-P<br>Nachwuchsförderung und<br><span class="boxed">mangement</span></div>

  <h1 class="headline">WIR BEGLEITEN<br>DICH AUF DEINEM<br>WEG ZUM PROFI</h1>

  <ul class="services services-right">
    <li><span class="title">Karriereplanung</span>Wir haben deine Karriere im Blick! In enger Absprache mit deinen Eltern und dir leiten wir die richtigen Maßnahmen und Schritte ein, um dein Ziel „Profifußballer“ zu realisieren.</li>
    <li><span class="title">Ständiger Ansprechpartner</span>Egal um welchen Themen es sich handelt, wir sind für dich da! Ein vertrauensvolles und freundschaftliches Verhältnis ist uns wichtig.</li>
    <li><span class="title">Rechtsberatung/Vertragsrecht</span>Juristendeutsch und Kleingedrucktes? Kein Problem! Wir helfen dir den Durchblick zu behalten und holen immer das Beste raus.</li>
  </ul>

  <ul class="services services-bottom col-1"><li><span class="title">Ausrüstung</span>Wir besorgen dir deine Ausrüstung! Unsere Beziehungen zu den großen Sportartikelherstellern ermöglichen den Abschluss von Ausrüsterverträ-<br>gen*.</li></ul>
  <ul class="services services-bottom col-2"><li><span class="title">Vorsorge</span>Verletzungen gehören leider zum Fußball dazu. Wir sichern dich ab, indem wir eine private Zusatzkrankenversicherung für dich abschließen.</li></ul>
  <ul class="services services-bottom col-3"><li><span class="title">Kooperationspartner/Netzwerk</span>Ob Entscheidungsträger oder Experte, wir kennen die richtigen Leute. Zusätzlich bieten wir dir eine große Bandbreite an Leistungen, die du jederzeit in Anspruch nehmen kannst**.</li></ul>

  <div class="brand"><span class="brand-dot"></span><span class="brand-name">SVR</span></div>

  <ul class="contact">
    <li><svg width="22" height="22" viewBox="0 0 22 22"><circle cx="11" cy="11" r="10" fill="none" stroke="var(--ink)" stroke-width="1.2"/><path d="M7.5 6.5l2 2-1 1.2c.6 1.4 1.5 2.3 2.8 2.8l1.2-1 2 2-1.2 1.3C10.5 14.8 7.2 11.5 6.2 7.7z" fill="var(--ink)"/></svg>07000/4821730</li>
    <li><svg width="22" height="22" viewBox="0 0 22 22"><circle cx="11" cy="11" r="10" fill="none" stroke="var(--ink)" stroke-width="1.2"/><rect x="6" y="7.5" width="10" height="7" fill="var(--ink)"/><path d="M6 7.5l5 4 5-4" fill="none" stroke="var(--white)" stroke-width="1"/></svg>info@svr-p.de</li>
    <li><svg width="22" height="22" viewBox="0 0 22 22"><circle cx="11" cy="11" r="10" fill="none" stroke="var(--ink)" stroke-width="1.2"/><circle cx="11" cy="11" r="5.5" fill="none" stroke="var(--ink)" stroke-width="1.2"/><path d="M5.5 11h11M11 5.5v11" stroke="var(--ink)" stroke-width="1"/></svg>www.svr-p.de</li>
  </ul>

  <div class="rule"></div>
  <p class="footnote">*Die Entscheidung über das Zustandekommen eines Ausrüstervertrags obliegt dem jeweiligen Sportartikelhersteller. Ist ein Abschluss aktuell nicht möglich, erhältst du von uns 2x pro Saison neue Fußballschuhe sowie weitere Ausrüstungsgegenstände.</p>
  <p class="footnote-extra">**Personal Training, Athletik-Training, Ernährungsberatung, Sportpsychologische Betreuung, uvm.</p>

  <div class="footer-bar bar-1"></div>
  <div class="footer-bar bar-2"></div>
  <div class="footer-bar bar-3"></div>
  <div class="footer-bar bar-4"></div>
</main>
</body>
</html>
```